Wordpress Web Design & Coding for velnoragroup.ca

We need a website for a new investment company that is visually grabbing and vibrant. We would like to see a web page that displays trust, growth and confidence. Needs to be responsive and mobile friendly for all browsers and coded for both Android & IOS.

Open to the number of pages and menu items. I selected 4 but if you feel the layout would work better with less I am open to this. Need to sell the people (management team/related businesses) and then show where the invested money will be going (upcoming projects).

Company Info:

Velnora is an investment company put together by a group of seasoned business professionals who have come together to combine decades of success in the real estate development, management, financing and medical services. The company will be a full service company offering turn key solutions for medical professionals.

Vel-Nora will focus on providing a full range of services via a group of distinct companies to deliver newly emerging needs of the medical community. The end goal will be to create complete solutions for individuals in the medical community. Our group has experience and success with the conceptualization, construction and financing of medical and dental clinic spaces. Vel-Nora Group will be established to accommodate all areas of the development and creation of clinics for medical professionals from building construction to equipment financing and administrations.

You can mention these companies and take photos from their websites. You can also use stock photos.

Our construction partner:
https://382bld.com/projects/

Our equipment leasing partner:
https://www.pordiva.com/

Our Management Team and medical partners

Gil Parkes
https://www.mysoundpoise.ca/

Milos Vendraker
https://www.qrtdentalservices.com/about-us

PROPOSED PROJECTS (see attachment for details)
Hollowmere Business Park
Cresfield Business Park
Mt. Corwin Ridge Professional

Investors

Investment

Sans Serif

Must have
• Wordpress – must be both desktop and mobile friendly with fast page load speed
Ability to edit after ourselves in Wordpress
Attractive home page with logo etc.
Logo colours are: for the blue the pantone color is #0355a3
and for the green is #8cc63f

Sections, about us, what we do/services we provide, contact us

```html
<!DOCTYPE html>
<html lang="en">
<head>
<meta charset="utf-8">
<title>Vel-Nora Group</title>
<link href="https://fonts.googleapis.com/css2?family=Roboto:wght@300;400;500;700&display=swap" rel="stylesheet">
<style>
:root{
  --blue:#0355a3;
  --blue-deep:#063f86;
  --green:#8cc63f;
  --light:#efefef;
  --text:#444;
  --navy:#0b1b37;
  --navy-deep:#06122a;
  --white:#fff;
}
*{margin:0;padding:0;box-sizing:border-box}
html,body{width:1200px;height:3644px;overflow:hidden}
body{position:relative;font-family:'Roboto',sans-serif;color:var(--text);background:var(--white)}
.abs{position:absolute}
a{color:inherit;text-decoration:none}

/* header */
.site-header{top:0;left:0;width:1200px;height:87px;background:var(--white);z-index:5}
.brand{left:35px;top:0;width:166px;height:113px;background:var(--white);border-radius:0 0 6px 6px;display:flex;flex-direction:column;align-items:center;justify-content:center;z-index:6}
.brand-name{font-weight:700;font-size:22px;color:var(--blue);letter-spacing:.5px}
.brand-sub{font-weight:700;font-size:14px;color:var(--blue);letter-spacing:1px}
.nav{left:320px;top:0;height:87px;display:flex;gap:0}
.nav a{display:block;height:87px;line-height:87px;padding:0 17px;font-size:11px;font-weight:500;color:#555}
.nav a.active{color:var(--green);border-bottom:2px solid var(--green)}
.call{left:886px;top:20px;display:flex;align-items:center;gap:10px}
.call-icon{width:44px;height:44px;border-radius:50%;background:var(--blue);display:flex;align-items:center;justify-content:center}
.call-num{font-size:21px;font-weight:700;color:var(--green);line-height:1}
.call-sub{font-size:12px;color:#666;margin-top:3px}

/* hero */
.hero{top:87px;left:0;width:1200px;height:525px}
.hero-copy{left:618px;top:175px;width:480px;color:var(--white)}
.hero-copy h1{font-weight:300;font-size:42px;line-height:1.2}
.hero-copy h1 strong{display:block;font-weight:700;color:var(--green);font-size:43px}
.hero-copy p{font-size:17px;line-height:31px;margin-top:28px;font-weight:300}
.hero-copy p b{font-weight:700}
.btn{display:inline-block;background:var(--green);color:var(--white);font-weight:500;border-radius:30px;text-align:center}
.hero-btn{margin-top:48px;width:136px;height:50px;line-height:50px;font-size:15px}

/* about */
.about{top:550px;left:0;width:1200px;height:560px;background:var(--light)}
.section-title{font-weight:400;font-size:30px;color:var(--blue)}
.rule{height:2px;background:var(--green);opacity:.7}
.about-title{left:137px;top:668px}
.about-rule{left:137px;top:724px;width:252px}
.about-copy{left:137px;top:750px;width:945px;font-size:13px;line-height:24px;color:#555}
.about-copy p+p{margin-top:18px}
.about-copy b{color:#333}
.about-btn{left:137px;top:972px;width:274px;height:40px;line-height:40px;font-size:13px}

/* what we do */
.services{top:1075px;left:0;width:1200px;height:735px}
.services-title{left:0;top:1160px;width:1200px;text-align:center;color:var(--white)}
.services-rule{left:437px;top:1217px;width:326px}
.services-copy{left:110px;top:1415px;width:520px;text-align:center;color:var(--white);font-size:23px;line-height:34px;font-weight:300}
.services-btn{left:253px;top:1538px;width:236px;height:50px;line-height:50px;font-size:15px}
.card{background:var(--white);border-radius:10px;display:flex;flex-direction:column;align-items:center;justify-content:center;text-align:center;color:var(--blue);font-weight:500;font-size:19px;line-height:26px;gap:14px}

/* team */
.team-title{left:0;top:1893px;width:1200px;text-align:center}
.team-rule{left:437px;top:1950px;width:326px}
.tile{width:192px;height:192px}
.photo{background:linear-gradient(160deg,#8a8f96,#4d5560)}
.member{background:var(--white);display:flex;flex-direction:column;align-items:center;justify-content:center;gap:10px}
.member-name{font-size:13px;font-weight:700;color:var(--blue)}
.member-co{font-size:20px;font-weight:400;color:#333;letter-spacing:1px}
.plus{width:18px;height:18px;border-radius:50%;background:var(--green);position:relative}
.plus::before,.plus::after{content:"";position:absolute;background:var(--white);left:50%;top:50%;transform:translate(-50%,-50%)}
.plus::before{width:9px;height:2px}.plus::after{width:2px;height:9px}
.plan{background:var(--blue);color:var(--white);font-size:19px;line-height:28px;padding:58px 18px}
.team-copy{left:620px;top:2392px;width:510px;font-size:13px;line-height:24px;color:#666}
.team-btn{left:801px;top:2468px;width:174px;height:40px;line-height:40px;font-size:13px}

/* projects */
.projects-title{left:0;top:2707px;width:1200px;text-align:center;color:var(--white)}
.project{width:320px;height:366px;background:var(--white);box-shadow:0 4px 18px rgba(0,0,0,.12);border-radius:4px;text-align:center}
.project-img{margin:14px auto 0;width:292px;height:222px}
.project h3{font-size:18px;font-weight:700;color:var(--blue);margin-top:30px}
.project small{display:block;font-size:11px;color:#777;margin-top:8px}
.project .plus{margin:16px auto 0}

/* footer */
.footer{top:3283px;left:0;width:1200px;height:300px;background:var(--navy);color:var(--white)}
.footer-bottom{top:3583px;left:0;width:1200px;height:61px;background:var(--navy-deep);color:var(--white);font-size:13px;text-align:center;line-height:61px}
.f-brand{left:150px;top:3385px;width:150px;text-align:center}
.f-brand .brand-name{color:var(--blue);font-size:26px}
.f-brand .brand-sub{color:var(--green);font-size:14px}
.socials{left:177px;top:3453px;display:flex;gap:6px}
.socials span{width:29px;height:29px;border-radius:4px;background:var(--blue)}
.f-col h4{font-size:16px;font-weight:400;margin-bottom:28px}
.f-col li{list-style:none;font-size:13px;line-height:28px}
.f-contact li{display:flex;gap:10px;line-height:24px;margin-bottom:4px}
</style>
</head>
<body>

<!-- header -->
<header class="abs site-header">
  <nav class="abs nav">
    <a href="#">Home</a><a class="active" href="#">About Us</a><a href="#">What We Do</a><a href="#">Our Projects</a><a href="#">Contact Us</a>
  </nav>
  <div class="abs call">
    <div class="call-icon"><svg width="18" height="18" viewBox="0 0 24 24"><path fill="#fff" d="M6.6 10.8a15 15 0 0 0 6.6 6.6l2.2-2.2c.3-.3.7-.4 1-.2 1.1.4 2.3.6 3.6.6.6 0 1 .4 1 1V20c0 .6-.4 1-1 1A17 17 0 0 1 3 4c0-.6.4-1 1-1h3.5c.6 0 1 .4 1 1 0 1.3.2 2.5.6 3.6.1.3 0 .7-.2 1z"/></svg></div>
    <div><div class="call-num">555-210-4870</div><div class="call-sub">Call us now!</div></div>
  </div>
</header>
<div class="abs brand"><span class="brand-name">VEL-NORA</span><span class="brand-sub">GROUP</span></div>

<!-- hero -->
<svg class="abs hero" viewBox="0 0 1200 525" preserveAspectRatio="none" role="img" aria-label="Modern medical office building photo with blue overlay">
  <defs><linearGradient id="heroG" x1="0" y1="0" x2="1" y2="1"><stop offset="0" stop-color="#0a3f85"/><stop offset=".5" stop-color="#1a5aa5"/><stop offset="1" stop-color="#06397a"/></linearGradient></defs>
  <path d="M0 0H1200V465Q600 600 0 463Z" fill="url(#heroG)"/>
</svg>
<div class="abs hero-copy">
  <h1>Invest in<strong>VEL-NORA Group</strong></h1>
  <p>Vel-Nora Group established to accommodate all areas of the development and creation of <b>clinics for medical professionals</b></p>
  <a class="btn hero-btn" href="#">About Us</a>
</div>

<!-- about -->
<section class="abs about" style="z-index:-1"></section>
<h2 class="abs section-title about-title">ABOUT US</h2>
<div class="abs rule about-rule"></div>
<div class="abs about-copy">
  <p><b>Velnora</b> is an investment company put together by a group of seasoned business professionals who have come together to combine decades of success in the real estate development, management, financing and medical services. The company will be a full service company offering turn key solutions for medical professionals.</p>
  <p><b>Velnora</b> will focus on providing a full range of services via a group of distinct companies to deliver newly emerging needs of the medical community. The end goal will be to create complete solutions for individuals in the medical community. Our group has experience and success with the conceptualization, construction and financing of medical and dental clinic spaces. Vel-Nora Group will be established to accommodate all areas of the development and creation of clinics for medical professionals from building construction to equipment financing and administrations.</p>
</div>
<a class="abs btn about-btn" href="#">Our Management Team &amp; Partners</a>

<!-- what we do -->
<svg class="abs services" viewBox="0 0 1200 735" preserveAspectRatio="none" role="img" aria-label="Medical office building and trees photo with blue overlay">
  <defs><linearGradient id="svcG" x1="0" y1="0" x2="0" y2="1"><stop offset="0" stop-color="#0a57ad"/><stop offset=".55" stop-color="#2a6cb8"/><stop offset="1" stop-color="#0652a6"/></linearGradient></defs>
  <path d="M0 50Q600 -40 1200 50V690Q600 770 0 690Z" fill="url(#svcG)"/>
</svg>
<h2 class="abs section-title services-title" style="color:#fff">WHAT WE DO</h2>
<div class="abs rule services-rule"></div>
<p class="abs services-copy">Vel-Nora Group established to accommodate all areas of the development and creation of clinics for medical professionals</p>
<a class="abs btn services-btn" href="#">Our Upcoming Projects</a>

<div class="abs card" style="left:648px;top:1341px;width:212px;height:218px">
  <svg width="76" height="72" viewBox="0 0 76 72" fill="none" stroke="#8cc63f" stroke-width="2"><path d="M20 70V8M30 70V8M20 18h10M20 32h10M20 46h10M20 60h10M10 8h56M25 2v6M10 8l15-6 15 6M60 8v24M52 32h16l-8 12z"/><path d="M6 70h30"/></svg>
  <span>Medical Building<br>Construction</span>
</div>
<div class="abs card" style="left:878px;top:1252px;width:205px;height:218px">
  <svg width="72" height="66" viewBox="0 0 72 66" fill="none" stroke="#8cc63f" stroke-width="2"><rect x="2" y="22" width="44" height="22" rx="2"/><circle cx="24" cy="33" r="6"/><path d="M8 14l30-10 8 18"/><ellipse cx="58" cy="38" rx="11" ry="4"/><path d="M47 38v20c0 2 5 4 11 4s11-2 11-4V38M47 46c0 2 5 4 11 4s11-2 11-4M47 54c0 2 5 4 11 4s11-2 11-4"/></svg>
  <span>Equipment<br>Financing</span>
</div>
<div class="abs card" style="left:878px;top:1490px;width:205px;height:218px">
  <svg width="70" height="66" viewBox="0 0 70 66" fill="none" stroke="#8cc63f" stroke-width="2"><rect x="4" y="10" width="62" height="54" rx="2"/><path d="M4 22h62M16 4v10M30 4v10M44 4v10M58 4v10"/><circle cx="16" cy="4" r="3"/><circle cx="30" cy="4" r="3"/><circle cx="44" cy="4" r="3"/><circle cx="58" cy="4" r="3"/><path d="M22 54V38h8v16M30 54V32h10v22M40 54V40h8v14M16 54h38"/></svg>
  <span>Construction<br>Administrations</span>
</div>

<!-- team -->
<h2 class="abs section-title team-title">OUR MANAGEMENT TEAM</h2>
<div class="abs rule team-rule"></div>

<div class="abs tile photo" style="left:192px;top:1993px" role="img" aria-label="Portrait photo of Rex Dunmore"></div>
<div class="abs tile member" style="left:384px;top:1993px"><span class="member-name">Rex Dunmore</span><span class="member-co">PORDIVA</span><span class="plus"></span></div>

<div class="abs tile photo" style="left:0;top:2185px" role="img" aria-label="Portrait photo of Milos Vendraker"></div>
<div class="abs tile member" style="left:192px;top:2185px"><span class="member-name">Milos Vendraker</span><span class="member-co">QRT</span><span class="plus"></span></div>
<div class="abs tile plan" style="left:384px;top:2185px">Select Your Investment Plan</div>
<div class="abs" style="left:576px;top:2202px;width:208px;height:158px;background:linear-gradient(160deg,#cfd6de,#6f7d8c)" role="img" aria-label="Professional building exterior photo"></div>
<div class="abs" style="left:784px;top:2202px;width:208px;height:158px;background:linear-gradient(160deg,#3f7fd0,#8c8f8a)" role="img" aria-label="Business park exterior photo"></div>
<div class="abs" style="left:992px;top:2202px;width:208px;height:158px;background:linear-gradient(160deg,#e4ddd0,#8e8373)" role="img" aria-label="Clinic interior reception photo"></div>

<div class="abs tile member" style="left:0;top:2377px"><span class="member-name">Dr. Gil Parkes</span><span class="member-co">soundpoise</span><span class="plus"></span></div>
<div class="abs tile photo" style="left:192px;top:2377px" role="img" aria-label="Portrait photo of Dr. Gil Parkes"></div>

<p class="abs team-copy">Lorem ipsum dolor sit amet, consectetur adipiscing elit. Ut elit tellus, luctus nec ullamcorper mattis, pulvinar dapibus leo.</p>
<a class="abs btn team-btn" href="#">Upcoming Projects</a>

<!-- projects -->
<svg class="abs" style="left:0;top:2650px" width="1200" height="310" viewBox="0 0 1200 310" preserveAspectRatio="none" role="img" aria-label="Building photo with blue overlay">
  <path d="M0 20Q600 -40 1200 20V310H0Z" fill="#0a57ad"/>
</svg>
<h2 class="abs section-title projects-title">UPCOMING PROJECTS</h2>

<article class="abs project" style="left:102px;top:2835px">
  <div class="project-img" style="background:linear-gradient(160deg,#e6e0d4,#7b7163)" role="img" aria-label="Office interior reception photo"></div>
  <h3>Hollowmere Business Park</h3><small>Office and light Industrial Building Project</small><div class="plus"></div>
</article>
<article class="abs project" style="left:440px;top:2835px">
  <div class="project-img" style="background:linear-gradient(170deg,#2f74cc,#cfd3d2 60%,#7d8a72)" role="img" aria-label="Business park rendering"></div>
  <h3>Cresfield Business Park</h3><small>Longford, British Colombia</small><div class="plus"></div>
</article>
<article class="abs project" style="left:777px;top:2835px">
  <div class="project-img" style="background:linear-gradient(160deg,#dfe4e8,#6c7e90)" role="img" aria-label="Professional services building photo"></div>
  <h3>Mt. Corwin Ridge Professional</h3><small>Professional Services Building</small><div class="plus"></div>
</article>

<!-- footer -->
<footer class="abs footer"></footer>
<div class="abs f-brand"><div class="brand-name">VEL-NORA</div><div class="brand-sub">GROUP</div></div>
<div class="abs socials"><span></span><span></span><span style="background:#c62828"></span></div>
<div class="abs f-col" style="left:360px;top:3345px;color:#fff">
  <h4>PARTNERS</h4>
  <ul><li>382 Builders</li><li>Pordiva Equipment Leasing</li><li>Sound Poise</li><li>QRT Dental Services</li></ul>
</div>
<div class="abs f-col" style="left:608px;top:3345px;color:#fff">
  <h4>RESOURCES</h4>
  <ul><li>Home</li><li>About Us</li><li>Projects</li><li>Contact Us</li></ul>
</div>
<div class="abs f-col f-contact" style="left:858px;top:3345px;color:#fff;width:240px">
  <h4>CONTACTS</h4>
  <ul>
    <li><svg width="10" height="14" viewBox="0 0 10 14" style="margin-top:5px;flex:none"><path fill="#8cc63f" d="M5 0a5 5 0 0 1 5 5c0 4-5 9-5 9S0 9 0 5a5 5 0 0 1 5-5zm0 3a2 2 0 1 0 0 4 2 2 0 0 0 0-4z"/></svg><span>Lorem ipsum dolor sit amet, consectetur adipiscing elit</span></li>
    <li><svg width="12" height="12" viewBox="0 0 24 24" style="margin-top:6px;flex:none"><path fill="#8cc63f" d="M6.6 10.8a15 15 0 0 0 6.6 6.6l2.2-2.2c.3-.3.7-.4 1-.2 1.1.4 2.3.6 3.6.6.6 0 1 .4 1 1V20c0 .6-.4 1-1 1A17 17 0 0 1 3 4c0-.6.4-1 1-1h3.5c.6 0 1 .4 1 1 0 1.3.2 2.5.6 3.6.1.3 0 .7-.2 1z"/></svg><span>555-318-6042</span></li>
    <li><svg width="12" height="10" viewBox="0 0 12 10" style="margin-top:7px;flex:none"><rect width="12" height="10" rx="1" fill="#8cc63f"/><path d="M0 1l6 4 6-4" stroke="#0b1b37" fill="none"/></svg><span>info@velnoragroup.ca</span></li>
  </ul>
</div>
<div class="abs footer-bottom">Copyright © 2020 VEL-NORA Group. All rights reserved.</div>

</body>
</html>
```